Home and Garden business needs a Facebook Design

We need a design for a Home and Garden business called Meadow and Hearth. Our main focus is on perennial plants and home décor. We want to project an image that's a combination of Clara Dunmores Keeping and Finer Rooms and Orchards. The main focus should be on perennial plants and gardening with a secondary emphasis on home décor. Our target customers are homeowners between the age of 30 and 65 with a strong passion for gardening and 'Do it Yourselfers'. Our logo is green and we would like to see any color combinations that go with the logo. The final design should communicate the joy and pride of improving your home and gardens.
Target Market(s)
Homeowners 30 - 65
Industry/Entity Type
Home And Garden
Requirements
Must have
- for an idea of what we are after please take a look at https://www.brindlepost.example/TallyBlooms
- https://www.brindlepost.example/claradunmore
- https://www.brindlepost.example/NookFieldHaven

```html
<!DOCTYPE html>
<html lang="en">
<head>
<meta charset="utf-8">
<title>Meadow &amp; Hearth — Cover</title>
<link rel="stylesheet" href="https://fonts.googleapis.com/css2?family=Montserrat:wght@500;700;800&family=Arimo:wght@400;700&display=swap">
<style>
  :root {
    --sky-top: #2f8fd9;
    --sky-mid: #4aa6e6;
    --sky-low: #6fb6e3;
    --foliage: #8a9a3a;
    --blossom: #d99aa6;
    --white: #ffffff;
    --leaf-green: #5aa82e;
    --nav-text: #4b4f56;
    --nav-active: #1d2129;
    --nav-line: #4267b2;
    --divider: #e5e6e9;
    --frame-line: #d3d6db;
  }
  * { box-sizing: border-box; margin: 0; padding: 0; }
  html, body { width: 1200px; height: 508px; overflow: hidden; background: var(--white); }
  .cover-canvas { position: relative; width: 1200px; height: 508px; overflow: hidden; font-family: "Montserrat", Arial, sans-serif; }

  .cover-photo {
    position: absolute; left: 0; top: 0; width: 1200px; height: 446px;
    background:
      radial-gradient(ellipse 420px 380px at 1000px 260px, var(--blossom) 0%, rgba(217,154,166,0.55) 45%, rgba(217,154,166,0) 75%),
      radial-gradient(ellipse 320px 460px at 30px 230px, var(--foliage) 0%, rgba(138,154,58,0.6) 45%, rgba(138,154,58,0) 80%),
      radial-gradient(ellipse 200px 220px at 300px 360px, rgba(170,180,70,0.7) 0%, rgba(170,180,70,0) 80%),
      linear-gradient(180deg, var(--sky-top) 0%, var(--sky-mid) 55%, var(--sky-low) 100%);
  }

  .cover-headline {
    position: absolute; left: 321px; top: 30px;
    color: var(--white); font-weight: 800; font-size: 61px; letter-spacing: 0.5px; line-height: 1.1;
  }
  .cover-tagline {
    position: absolute; left: 321px; top: 112px; width: 560px;
    color: var(--white); font-weight: 700; font-size: 23.5px; line-height: 1.42;
  }

  .page-name {
    position: absolute; left: 321px; top: 322px;
    color: var(--white); font-weight: 800; font-size: 31px;
    text-shadow: 0 1px 4px rgba(0,0,0,0.45);
  }
  .page-category {
    position: absolute; left: 321px; top: 369px;
    color: var(--white); font-weight: 700; font-size: 23px;
    text-shadow: 0 1px 4px rgba(0,0,0,0.45);
  }

  .profile-frame {
    position: absolute; left: 20px; top: 240px; width: 254px; height: 253px;
    background: var(--white); border: 1px solid var(--frame-line);
    box-shadow: 0 1px 2px rgba(0,0,0,0.2);
    display: flex; flex-direction: column; align-items: center; justify-content: center; gap: 16px;
    z-index: 2;
  }
  .brand-dot { width: 62px; height: 62px; border-radius: 50%; background: var(--leaf-green); }
  .brand-name {
    font-family: "Montserrat", Arial, sans-serif; font-weight: 700; font-size: 19px;
    color: var(--leaf-green); letter-spacing: 0.3px;
  }

  .page-nav {
    position: absolute; left: 0; top: 446px; width: 1200px; height: 62px;
    background: var(--white);
    font-family: "Arimo", Helvetica, Arial, sans-serif; font-size: 20px; color: var(--nav-text);
  }
  .nav-tab { position: absolute; top: 0; height: 62px; display: flex; align-items: center; }
  .nav-tab.is-active { color: var(--nav-active); font-weight: 700; }
  .nav-tab.is-active::after {
    content: ""; position: absolute; left: -2px; right: -2px; bottom: 0; height: 4px; background: var(--nav-line);
  }
  .nav-divider { position: absolute; top: 12px; width: 1px; height: 38px; background: var(--divider); }
  .nav-caret { width: 10px; height: 6px; margin-left: 8px; }
</style>
</head>
<body>
  <main class="cover-canvas">
    <div class="cover-photo" role="img" aria-label="Pink cherry blossom branches and yellow-green spring foliage against a clear blue sky"></div>

    <h1 class="cover-headline">Do it Yourselfers</h1>
    <p class="cover-tagline">Lorem ipsum dolor sit amet, consectetur adipisicing elit, sed do eiusmod</p>

    <div class="profile-frame">
      <span class="brand-dot" aria-hidden="true"></span>
      <span class="brand-name">Meadow &amp; Hearth</span>
    </div>

    <h2 class="page-name">Meadow &amp; Hearth</h2>
    <p class="page-category">Public Figure</p>

    <nav class="page-nav">
      <span class="nav-tab is-active" style="left:281px;">Timeline</span>
      <span class="nav-divider" style="left:385px;"></span>
      <span class="nav-tab" style="left:409px;">About</span>
      <span class="nav-divider" style="left:483px;"></span>
      <span class="nav-tab" style="left:507px;">Photos</span>
      <span class="nav-divider" style="left:591px;"></span>
      <span class="nav-tab" style="left:615px;">Reviews</span>
      <span class="nav-divider" style="left:713px;"></span>
      <span class="nav-tab" style="left:737px;">More
        <svg class="nav-caret" viewBox="0 0 10 6" aria-hidden="true"><path d="M0 0h10L5 6z" fill="currentColor"/></svg>
      </span>
    </nav>
  </main>
</body>
</html>
```